Bright Sprout Learning Centre website redesign

Our website (which we have only just converted to wordpress) is just not good enough for my liking. Our centre offers classes for babies aged from 6 months to 7 years old in the middle east. Whilst our program is formal in the way that the practise deals with learning in hemispheres of the brain - the site should look more fun and a bit more approachable and attractive to families.
I like the site www.tallowpine.com or www.corvidlane.com from this region - I like the way that you land on home page with images and a quote rather than all this information coming at you and you not knowing where to click.
I want a fun and appealing site that features info about the program, class timetable, shop, news and events, gallery, blog posts etc…
I am really open to a complete redesign and just want something that looks professional but is fun and gets the information out quickly! Please look at www.brightsprout.ae for current site design

```html
<!DOCTYPE html>
<html lang="en">
<head>
<meta charset="utf-8">
<title>Bright Sprout Learning Centre</title>
<link href="https://fonts.googleapis.com/css2?family=Open+Sans:wght@400;600;700&family=Bree+Serif&family=Kalam:wght@700&display=swap" rel="stylesheet">
<style>
:root{
  --orange:#f39a3b;
  --blue:#4f8aa3;
  --navy:#2a4a66;
  --sky:#e6f1f9;
  --band:#d2e5f4;
  --text:#333;
  --white:#fff;
}
*{box-sizing:border-box;margin:0;padding:0}
html,body{width:728px;height:1200px;overflow:hidden}
body{position:relative;background:var(--sky);font-family:"Open Sans",Arial,sans-serif;color:var(--text)}
.abs{position:absolute}
a{color:inherit;text-decoration:none}

.top-tab{left:395px;top:0;width:247px;height:18px;background:var(--orange);border-radius:0 0 12px 12px;color:var(--white);font-size:7.5px;display:flex;justify-content:center;align-items:center;gap:5px}
.brand{left:87px;top:14px;width:68px;height:80px;display:flex;flex-direction:column;align-items:center;justify-content:center;gap:6px}
.brand .mark{width:40px;height:40px;border-radius:50%;background:var(--orange)}
.brand .name{font-weight:700;font-size:9px;color:var(--blue);text-align:center;line-height:1.1}
.header-photo{left:206px;top:40px;width:244px;height:41px;background:linear-gradient(90deg,#8aa6b8,#c9a88e,#e3d2c2,#9fb4c4);border:1px solid #999}
.phone{left:514px;top:29px;display:flex;align-items:center;gap:6px;font-size:12px;color:#333}
.follow{left:496px;top:52px;display:flex;align-items:center;gap:3px;font-size:8.5px;font-weight:700}
.follow i{display:inline-block;width:12px;height:12px;border-radius:2px;background:var(--blue)}
.follow i:nth-child(3){background:#c84a4a}
.follow i:nth-child(4){background:#6b4a3a}
.search{left:478px;top:76px;width:165px;height:18px;background:var(--white);border:1px solid #bbb;border-radius:2px;font-size:9px;color:#666;padding:2px 6px}
.search svg{position:absolute;right:4px;top:2px}

.nav{left:85px;top:103px;width:559px;height:23px;background:var(--blue);border-radius:3px;display:flex;font-size:9px;color:var(--white)}
.nav a{padding:0 7px;display:flex;align-items:center;border-right:1px solid #6d9fb5}
.nav a.active{background:var(--orange);padding:0 12px;border-radius:3px 0 0 3px}

.hero{left:0;top:133px;width:728px;height:226px;background:linear-gradient(120deg,#d9cfc2 0%,#b9a392 35%,#e8e1d7 60%,#8a6e62 100%)}
.hero-curve{left:0;top:318px}
.headline{left:86px;top:250px;font-family:"Kalam",cursive;font-weight:700;font-size:29px;line-height:36px;color:#2b2b2b}
.age-star{left:304px;top:246px}
.dots{left:327px;top:345px;display:flex;gap:5px}
.dots span{width:10px;height:10px;border-radius:50%;border:1.5px solid #fff;box-shadow:0 0 1px #999}
.dots span.on{background:var(--orange);border-color:var(--orange)}

.welcome{left:0;top:366px;width:728px;text-align:center;font-family:"Bree Serif",serif;font-weight:400;font-size:14px;color:#222}
.welcome b{font-weight:400;color:var(--blue)}
.rule{left:85px;top:392px;width:559px;border-top:1px dotted #d96a3a}
.intro{left:90px;top:402px;width:550px;text-align:center;font-size:8.4px;line-height:14px}
.intro strong{color:#111}

.band{left:0;top:510px;width:728px;height:482px;background:var(--band)}
.feature{top:457px;width:180px;text-align:center}
.feature .halo{width:104px;height:104px;margin:0 auto;border-radius:50%;background:#dcebf7;display:flex;align-items:center;justify-content:center}
.feature .icon{width:90px;height:90px;border-radius:50%;background:var(--orange);display:flex;align-items:center;justify-content:center}
.feature h3{margin-top:4px;font-weight:400;font-size:12.5px;color:var(--orange)}
.feature p{margin-top:6px;font-size:7.7px;line-height:14.2px;color:#333}
.read{top:652px;font-size:8px;color:var(--blue);display:flex;align-items:center;gap:4px}
.read i{width:9px;height:9px;border-radius:50%;background:#888;display:inline-block}
.sep{left:85px;top:680px;width:559px;border-top:1px solid #c6d8e6}
.ad{left:85px;top:695px;width:559px;height:78px;background:linear-gradient(90deg,#f2efe7 0%,#f5e15a 35%,#f8e02a 100%);border:1px solid #bbb}

.gallery-title{left:85px;top:795px;font-family:"Bree Serif",serif;font-weight:400;font-size:11.5px;color:#222}
.gallery-title b{font-weight:400;color:var(--blue)}
.gallery{left:85px;top:827px;width:360px;height:135px;background:#e8f1f9;border-radius:6px}
.thumb{top:843px;width:89px;height:102px;border-radius:6px;border:1px solid #888}
.arrow{width:13px;height:13px;border-radius:50%;background:#f4f4f4;border:1px solid #ccc;display:flex;align-items:center;justify-content:center;font-size:8px;color:#555}

.tweets{left:479px;top:806px;width:163px;height:154px;background:var(--white);border:1px solid #a9c4d6}
.tweets .head{height:17px;background:var(--blue);color:var(--white);font-size:8px;font-weight:700;padding:3px 7px}
.tweet{display:flex;gap:5px;padding:6px 5px 5px 5px;font-size:7px;line-height:10px}
.tweet i{flex:none;width:28px;height:26px;background:#b9625a}
.tweet + .tweet{border-top:1px dashed #888;margin:0 5px;padding-left:0;padding-right:0}
.tweets .foot{display:flex;justify-content:space-between;align-items:center;padding:2px 5px;font-size:7px}
.tweets .foot b{color:var(--blue);font-size:10px}
.tweets .foot a{color:var(--blue);text-decoration:underline}
.bird{left:613px;top:792px;width:26px;height:26px;border-radius:50%;background:#3a8fd3}

.talk-tab{left:85px;top:976px;width:178px;height:16px;border-radius:4px 4px 0 0;font-size:9px;font-weight:600;padding:1px 12px;color:#222;background:#f0f6fb;white-space:nowrap}
.press{left:0;top:992px;width:728px;height:41px;background:var(--white);display:flex;align-items:center;justify-content:center;gap:18px;font-weight:700;font-size:10px;color:var(--navy)}
.press .arrow{background:var(--white)}

.footer{left:0;top:1033px;width:728px;height:167px;background:var(--blue)}
.foot-col{color:var(--white)}
.foot-title{font-weight:600;font-size:10px;letter-spacing:.3px;line-height:14px}
.links{left:86px;top:1047px}
.links ul{list-style:none;margin-top:7px;font-size:7.5px;line-height:13.5px}
.vline{top:1047px;height:140px;border-left:1px solid #6d9fb5}
.contact{left:175px;top:1047px;width:174px}
.contact .field{margin-top:5px;height:13px;background:var(--white);border:1px solid #ccc;border-radius:2px;font-size:6.5px;color:#999;padding:1px 4px}
.contact .field.first{margin-top:8px}
.contact .field.big{height:32px}
.contact .submit{margin-top:9px;display:inline-block;background:var(--orange);color:var(--white);font-size:8.5px;font-weight:700;padding:2px 10px;border-radius:3px}
.testimonials{left:377px;top:1047px;width:170px}
.testimonials .nav-arrows{position:absolute;right:4px;top:0;font-size:10px;font-weight:700}
.testimonials p{margin-top:8px;font-size:7.2px;line-height:13.5px;font-style:italic}
.testimonials .who{margin-top:3px;font-size:8.5px;font-weight:700;line-height:10px}
.testimonials .role{font-size:8px;line-height:10px}
.f-brand{left:575px;top:1046px;width:70px;height:86px;display:flex;flex-direction:column;align-items:center;justify-content:center;gap:5px;color:var(--white)}
.f-brand .mark{width:36px;height:36px;border-radius:50%;background:#e7eef3}
.f-brand .name{font-weight:700;font-size:9px;text-align:center;line-height:1.1}
.f-social{left:574px;top:1144px;display:flex;gap:3px}
.f-social i{width:12px;height:12px;border-radius:2px;background:#dde9f1}
.copy{left:566px;top:1164px;width:88px;text-align:center;font-size:7.5px;line-height:10px;color:var(--white)}
</style>
</head>
<body>

<nav class="abs top-tab"><a>The Program</a>|<a>Class Timetable</a>|<a>Our Location</a>|<a>Contact Us</a></nav>

<div class="abs brand"><span class="mark"></span><span class="name">Bright Sprout</span></div>
<div class="abs header-photo" role="img" aria-label="Collage of family and classroom photos"></div>

<div class="abs phone">
  <svg width="16" height="16" viewBox="0 0 16 16"><circle cx="8" cy="8" r="7.2" fill="none" stroke="#4f8aa3" stroke-width="1.3"/><path d="M5.5 4.5l1.5 0 .7 2-1 .8c.5 1 1.2 1.7 2.2 2.2l.8-1 2 .7v1.5c-3.5.4-6.6-2.7-6.2-6.2z" fill="#4f8aa3"/></svg>
  +971 (0) 40001234
</div>
<div class="abs follow">Follow Us On:&nbsp;<i></i><i></i><i></i><i></i><i></i></div>
<div class="abs search">Search
  <svg width="13" height="13" viewBox="0 0 13 13"><circle cx="5.5" cy="5.5" r="4.3" fill="none" stroke="#777" stroke-width="1.2"/><path d="M8.6 8.6l3.6 3.6" stroke="#777" stroke-width="1.4"/></svg>
</div>

<nav class="abs nav">
  <a class="active">Home</a><a>The Program »</a><a>Classes »</a><a>Media</a><a>Our Location</a><a>Blog</a><a>About Us »</a><a>Shop</a><a style="border:0">Contact Us</a>
</nav>

<div class="abs hero" role="img" aria-label="Mothers and babies playing together on a classroom mat"></div>
<svg class="abs hero-curve" width="728" height="45" viewBox="0 0 728 45"><path d="M0 40 Q364 -30 728 40 V45 H0Z" fill="#e6f1f9"/></svg>
<h1 class="abs headline">The best head start<br>for your child</h1>
<svg class="abs age-star" width="96" height="86" viewBox="0 0 96 86">
  <polygon points="48,3 59,31 91,32 66,51 75,82 48,64 21,82 30,51 5,32 37,31" fill="#f6d6b2" fill-opacity=".75" stroke="#f0a868" stroke-width="2"/>
  <text x="48" y="45" text-anchor="middle" font-family="Bree Serif, serif" font-size="14" fill="#e38b3c">AGE</text>
  <text x="48" y="58" text-anchor="middle" font-family="Kalam, cursive" font-size="7" fill="#e38b3c" transform="rotate(-12 48 58)">6 Months-7 Years</text>
</svg>
<div class="abs dots"><span class="on"></span><span></span><span></span><span></span></div>

<h2 class="abs welcome">WELCOME TO <b>BRIGHT SPROUT</b></h2>
<div class="abs rule"></div>
<p class="abs intro">The Bright Sprout Accelerated Learning Centre in Dubai offers whole brain training for children from 6 months of age with the goal of promoting a balance in actively using both hemispheres of the brain. Hana Rashed was raised in Sydney, Australia. She became passionate about education after the birth of her first daughter Mira in 2008. Hana launched the successful business Nest ......<strong>More</strong></p>

<div class="abs band"></div>

<section class="abs feature" style="left:96px">
  <div class="halo"><div class="icon">
    <svg width="40" height="56" viewBox="0 0 40 56"><path d="M8 0v34M32 0v34" stroke="#fff" stroke-width="2"/><rect x="5" y="34" width="30" height="4" rx="2" fill="#fff"/><circle cx="20" cy="18" r="5" fill="#fff"/><path d="M13 34c0-8 3-11 7-11s7 3 7 11zM14 38l-4 14M26 38l4 14" stroke="#fff" stroke-width="3" fill="#fff"/></svg>
  </div></div>
  <h3>About Program</h3>
  <p>Our centre offers classes for babies aged from 6 months to 7 years old in the middle east. Whilst our program is formal in the way that the practice deals with learning</p>
</section>
<a class="abs read" style="left:151px"><i></i>Read More</a>

<section class="abs feature" style="left:283px">
  <div class="halo"><div class="icon">
    <svg width="54" height="54" viewBox="0 0 54 54"><rect x="12" y="14" width="38" height="36" rx="2" fill="none" stroke="#fff" stroke-width="3"/><g fill="#fff"><rect x="22" y="26" width="5" height="5"/><rect x="30" y="26" width="5" height="5"/><rect x="38" y="26" width="5" height="5"/><rect x="22" y="34" width="5" height="5"/><rect x="30" y="34" width="5" height="5"/><rect x="38" y="34" width="5" height="5"/><rect x="22" y="42" width="5" height="4"/><rect x="30" y="42" width="5" height="4"/></g><circle cx="16" cy="16" r="13" fill="#f39a3b" stroke="#fff" stroke-width="3"/><path d="M16 8v8h6" stroke="#fff" stroke-width="2.5" fill="none"/></svg>
  </div></div>
  <h3>Class Time Table</h3>
  <p>The Bright Sprout Centre in Learning Quarter, Dubai is open Sunday – Thursday and on Saturday. Classes take place between 9.30am and 5pm.</p>
</section>
<a class="abs read" style="left:342px"><i></i>Read More</a>

<section class="abs feature" style="left:460px">
  <div class="halo"><div class="icon">
    <svg width="58" height="50" viewBox="0 0 58 50"><circle cx="29" cy="9" r="8" fill="#fff"/><path d="M3 22h22l4 4 4-4h22v26H33l-4 2-4-2H3z" fill="#fff"/><path d="M9 28h14M9 33h14M9 38h14M35 28h14M35 33h14M35 38h14" stroke="#f39a3b" stroke-width="1.5"/></svg>
  </div></div>
  <h3>News &amp; Events</h3>
  <p><b>Posted on 7 April 2014</b><br>Abracadabra! It's the Bright Sprout end of Term 2 Party! Join us for a Free show hosted by Club</p>
</section>
<a class="abs read" style="left:526px"><i></i>Read More</a>

<div class="abs sep"></div>
<div class="abs ad" role="img" aria-label="Family festival advertising banner with a smiling child"></div>

<h2 class="abs gallery-title">PHOTO <b>GALLERY</b></h2>
<div class="abs gallery"></div>
<span class="abs arrow" style="left:92px;top:893px">‹</span>
<div class="abs thumb" style="left:116px;background:linear-gradient(135deg,#c9b2a4,#8e9bb0)" role="img" aria-label="Mother holding a baby in class"></div>
<div class="abs thumb" style="left:221px;background:linear-gradient(135deg,#8fa7c2,#e0b74a)" role="img" aria-label="Teacher reading to a group of children"></div>
<div class="abs thumb" style="left:326px;background:linear-gradient(135deg,#b79d7e,#d4b7c0)" role="img" aria-label="Two children reading books on the floor"></div>
<span class="abs arrow" style="left:425px;top:893px">›</span>

<aside class="abs tweets">
  <div class="head">LATEST UPDATES</div>
  <div class="tweet"><i></i><div>@brightsprout Lorem ipsum dolor sit amet, consectetuer ad Lorem ipiscing elit Lorem ipsum<br>2 hours ago</div></div>
  <div class="tweet"><i></i><div>@brightsprout Lorem ipsum dolor sit amet, consectetuer ad Lorem ipiscing elit Lorem ipsum<br>2 hours ago</div></div>
  <div class="foot"><b>Chirpline</b><a>Join the conversation</a></div>
</aside>
<div class="abs bird" role="img" aria-label="Small bird mascot"></div>

<div class="abs talk-tab">Who's talking about Bright Sprout?</div>
<div class="abs press">
  <span class="arrow">‹</span>
  <span>Weekday Post</span><span>Gulf Channel</span><span>Radio 96.4</span><span>The Herald Daily</span><span>City Kids Guide</span><span>Coast Woman</span>
  <span class="arrow">›</span>
</div>

<footer class="abs footer"></footer>
<div class="abs foot-col links">
  <h4 class="foot-title">Quick Links</h4>
  <ul><li>&gt; Home</li><li>&gt; The Program</li><li>&gt; Classes</li><li>&gt; Media</li><li>&gt; Our Location</li><li>&gt; Blog</li><li>&gt; About Us</li><li>&gt; Shop</li><li>&gt; Contact Us</li></ul>
</div>
<div class="abs vline" style="left:159px"></div>
<form class="abs foot-col contact">
  <h4 class="foot-title">Quick Contact</h4>
  <div class="field first">Name</div>
  <div class="field">Email</div>
  <div class="field">Phone</div>
  <div class="field big">Comments :</div>
  <span class="submit">Submit</span>
</form>
<div class="abs vline" style="left:362px"></div>
<div class="abs foot-col testimonials">
  <h4 class="foot-title">Client Testimonials</h4>
  <span class="nav-arrows">&lt; &gt;</span>
  <p>“ Lorem ipsum dolor sit amet, consectetuer ad Lorempiscing elit, sed diam nonummy nibh euismod Thistincidunt ut laoreet dolore magna aliquam erat Loremvolutpat. Ut wisi enim ad minim veniam, quis no Lorem strud exerci tation ullamcorper aliquam erat Loremvolutpat. Ut wisi enim ad minim veniam, quis no ”</p>
  <div class="who">Lorem ipsum</div>
  <div class="role">Lorem ipsum</div>
</div>
<div class="abs vline" style="left:561px"></div>
<div class="abs f-brand"><span class="mark"></span><span class="name">Bright Sprout</span></div>
<div class="abs f-social"><i></i><i></i><i></i><i></i><i></i></div>
<div class="abs copy">© 2014 Bright Sprout.<br>All right reserved.</div>

</body>
</html>
```